Striking new Advert required for Commercial Real Estate Agency

We need a a NEW newspaper advertisement for the marketing of a large commercial property (a Backpackers lodge)

Dimensions are to be width of 101mm and height of 100mm (10cms)

Our key design statement for this advert is clean, modern and minimalist design, with accents of 'HOT PINK' colour to remove it from looking too boring, perhaps in the area of the contact icons. The heirachy of the advert is outlined in the attached ADVERTISEMENT TEXT FILE.

Our company name is THE MERIDAL COLLECTIVE, and we want our brand to appear professional yet classy in it's design style (sort of like an advertising or design agency)

We have two logo options below, one more square in its layout (which we prefer) and the other more rectangular, which may be better suited for the layout. We are not adverse to the logo being reversed (white text on black), along with other key element areas such as the main advert heading and the "FOR SALE" part, and think this would be a good option.
There are two photos attached to be included in the advert.

We have attached an example of an old advert that we did, which we DID NOT LIKE, and which was for a smaller width than the one we need (it is only 65% of the width of this one). WE have also atached a file showing layout of some of our competitors adverts, which we dont think are too good either.

We are really open for ideas, but have time pressures, so please come back with any questions as soon as you can, if needed.

Thank you
Updates

Thank you for the great and diverse designs. There are a few standout options, but one style that we prefer most.

Target Market(s)

We are wanting this newspaper advertisement to attract interest from real estat e developers, investors and motel/lodge owners, along with other high nett worth individuals

Industry/Entity Type

Real Estate

Font styles to use
Serif
Sans Serif

Colors
1b1b1b
a54499
474747
fbfbfb

Requirements
Must have
• Clean modern look, predominantly monochromatic or black and white, with the hot pink accent somewhere, as mentioned above.
• All the contents of the TEXT provided, perhaps with additional space to add a little more if needed, Please advise if you think we dont have enough space for all of the TEXT
Should not have
• Script like fonts
• Cartoonish characters
• a 'cheap' look

```html
<!DOCTYPE html>
<html lang="en">
<head>
<meta charset="utf-8">
<title>Marlowe's Lodge – For Sale</title>
<link rel="stylesheet" href="https://fonts.googleapis.com/css2?family=Archivo+Black&family=Encode+Sans+Condensed:wght@400;600;700&family=Montserrat:wght@400;500&display=swap">
<style>
  :root {
    --ink: #1b1b1b;
    --accent: #a54499;
    --slate: #474747;
    --paper: #fbfbfb;
    --white: #ffffff;
  }
  * { margin: 0; padding: 0; box-sizing: border-box; }
  html, body { width: 1200px; height: 1186px; overflow: hidden; background: var(--paper); }
  .advert {
    position: relative; width: 1200px; height: 1186px; overflow: hidden;
    background: var(--white); color: var(--ink);
    font-family: "Encode Sans Condensed", "Arial Narrow", sans-serif;
  }
  .sale-banner {
    position: absolute; left: 0; top: 0; width: 1200px; height: 126px;
    background: var(--accent); display: flex; align-items: center; justify-content: center;
  }
  .sale-banner h1 {
    font-family: "Archivo Black", "Arial Black", sans-serif;
    font-size: 112px; letter-spacing: 6px; line-height: 1; color: var(--white);
    text-shadow: 6px 6px 0 var(--ink); margin-left: -10px;
  }
  .property-photo {
    position: absolute; left: 0; top: 126px; width: 1200px; height: 510px;
    background: linear-gradient(170deg, #b9c1c4 0%, #d9dcd8 30%, #8e948f 55%, #6f7d5a 80%, #9fae4a 100%);
  }
  .address-band {
    position: absolute; left: 0; top: 636px; width: 1200px; height: 66px;
    background: var(--accent); display: flex; align-items: center; justify-content: center;
  }
  .address-band h2 {
    font-size: 42px; font-weight: 700; color: var(--white); letter-spacing: -0.5px;
    text-shadow: 2px 2px 0 var(--ink);
  }
  .details { position: absolute; left: 38px; top: 704px; width: 1140px; }
  .details .lead { font-size: 31px; font-weight: 700; line-height: 44px; letter-spacing: -0.3px; white-space: nowrap; }
  .details ul { list-style: none; margin-top: 0; }
  .details li {
    position: relative; font-size: 28px; line-height: 41px; height: 41px; padding-left: 30px;
    white-space: nowrap;
  }
  .details li.two-line { height: 82px; }
  .details li::before {
    content: ""; position: absolute; left: 2px; top: 14px; width: 13px; height: 13px;
    border-radius: 50%; background: var(--ink);
  }
  .details sup { font-size: 0.6em; line-height: 0; vertical-align: 0.6em; }
  .details li .wrap { padding-left: 7px; }
  .tender {
    position: absolute; left: 38px; top: 972px; font-size: 28px; font-weight: 700;
    letter-spacing: 3px; color: var(--accent);
  }
  .agent-label { position: absolute; left: 38px; top: 1016px; font-size: 33px; letter-spacing: -0.3px; }
  .agent-name { position: absolute; left: 38px; top: 1060px; font-size: 38px; font-weight: 700; letter-spacing: -0.5px; }
  .brand { position: absolute; left: 540px; top: 972px; width: 630px; height: 130px; }
  .brand-square { position: absolute; left: 0; top: 10px; width: 96px; height: 96px; border: 6px solid var(--ink); }
  .brand-rule { position: absolute; left: 122px; top: 0; width: 3px; height: 116px; background: var(--ink); }
  .brand-name {
    position: absolute; left: 146px; top: 14px; width: 480px;
    font-family: "Montserrat", sans-serif; font-weight: 500; font-size: 36px; line-height: 1.2;
    color: var(--ink); letter-spacing: 1px;
  }
  .brand-web {
    position: absolute; left: 190px; top: 108px;
    font-family: "Montserrat", sans-serif; font-weight: 500; font-size: 21px; color: var(--accent);
  }
  .contact-bar {
    position: absolute; left: 0; top: 1110px; width: 1200px; height: 76px;
    background: var(--slate); display: flex; align-items: center; gap: 34px; padding-left: 36px;
    color: var(--white); font-size: 39px; font-weight: 700; letter-spacing: -0.3px; white-space: nowrap;
  }
  .contact-item { display: flex; align-items: center; gap: 10px; }
  .contact-item svg { width: 28px; height: 28px; fill: none; stroke: var(--white); stroke-width: 2; }
</style>
</head>
<body>
<main class="advert">
  <header class="sale-banner"><h1>FOR SALE</h1></header>

  <div class="property-photo" role="img" aria-label="Aerial photograph of a large two-storey white weatherboard lodge with grey roofs, parked cars and surrounding hillside houses and trees"></div>

  <div class="address-band"><h2>Marlowe’s Lodge, 27 Harcourt Street, Mount Victoria</h2></div>

  <section class="details">
    <p class="lead">This Old Beauty has served many, and is now ripe for development. One of Mt Vic’s<br>largest land areas, now offered with vacant possession, with key details being:</p>
    <ul>
      <li>Large Land area of 2076m<sup>2</sup> with elevated sunny position and great outlook + access from Linden&nbsp; Street</li>
      <li>Existing Backpackers Lodge of 970m<sup>2</sup> providing multiple rooms with amenity areas</li>
      <li class="two-line">Four adjacent sites also available, taking total land area to 4452m<sup>2</sup>, an unprecedented Land Offering in<br><span class="wrap">this popular cuity fringe location</span></li>
    </ul>
  </section>

  <p class="tender">Now Selling by Closed Tender</p>
  <p class="agent-label">Contact the Sole Agent :</p>
  <p class="agent-name">Daniel Forbes</p>

  <div class="brand">
    <div class="brand-square"></div>
    <div class="brand-rule"></div>
    <p class="brand-name">THE MERIDAL<br>COLLECTIVE</p>
    <p class="brand-web">www.meridalcollective.co.nz</p>
  </div>

  <footer class="contact-bar">
    <span class="contact-item">
      <svg viewBox="0 0 24 24" aria-hidden="true"><path d="M4 9c0-3 4-4 8-4s8 1 8 4l-3 1-1-2H8L7 10z"/><rect x="6" y="11" width="12" height="8" rx="1"/></svg>
      (04) 555 0182
    </span>
    <span class="contact-item">
      <svg viewBox="0 0 24 24" aria-hidden="true"><circle cx="12" cy="12" r="10"/><path d="M9 7l2 3-1 1c1 2 2 3 3 3l1-1 3 2c-1 2-3 2-5 1-2-1-4-3-5-5-1-2 0-4 2-4z"/></svg>
      (021) 555 0147
    </span>
    <span class="contact-item">
      <svg viewBox="0 0 24 24" aria-hidden="true"><rect x="2" y="5" width="20" height="14"/><path d="M2 5l10 8 10-8M2 19l7-7M22 19l-7-7"/></svg>
      daniel@meridalcollective.co.nz
    </span>
  </footer>
</main>
</body>
</html>
```